"Thank You" flyer design

We need a "thank you" flyer that will be sent out with all our products.
a6 size landscape,
We manufacture personalised shaped signs.
I've attached a rough idea of what we are after, but would like it to be improved upon with some artistic flare..

Side one - We would like the flyer to have a simple message - "thank you for shopping with us"

Side two - we would also like our logo and a union jack made in the UK badge and our address and contact details with our website www.lumkinprints.co.uk being the most prominent..

We are after a simple bold design what would be printed on a small a6 card that people might hopefully want to keep, so the end design needs to be pretty cool.

Industry/Entity Type

Shopping

Font styles to use
Serif
Sans Serif

```html
<!DOCTYPE html>
<html lang="en">
<head>
<meta charset="utf-8">
<title>Lumkin Prints – Thank You Flyer</title>
<link rel="stylesheet" href="https://fonts.googleapis.com/css2?family=Arimo&family=Josefin+Sans:wght@700&family=Montserrat:wght@600&display=swap">
<style>
  :root {
    --ink: #111111;
    --paper: #ffffff;
    --rule: #222222;
    --sign-frame: #2e2e2e;
    --sign-edge: #9a9a9a;
    --accent-mark: #e0148a;
    --badge-red: #d42a2a;
    --brick-light: #e0875a;
    --brick-mid: #cf6f3a;
    --brick-dark: #9c4a22;
    --tile-light: #f2f2ee;
    --tile-mid: #8fae62;
    --tile-dark: #3b4a2e;
  }
  * { box-sizing: border-box; margin: 0; padding: 0; }
  html, body { width: 1200px; height: 850px; overflow: hidden; background: var(--paper); }
  .sheet { position: relative; width: 1200px; height: 850px; }
  .card {
    position: absolute; left: 0; width: 1200px; height: 425px;
    border: 1px solid var(--rule);
  }
  .card--top { top: 0; }
  .card--bottom { top: 425px; }
  .card--brick { --wall-a: var(--brick-light); --wall-b: var(--brick-mid); --wall-c: var(--brick-dark);
    --dash-a: #f0c8a0; --dash-b: #9c4a22; }
  .card--tile { --wall-a: var(--tile-light); --wall-b: var(--tile-mid); --wall-c: var(--tile-dark);
    --dash-a: #3b4a2e; --dash-b: #8fae62; }

  .card__front, .card__back { position: absolute; top: 0; height: 100%; }
  .card__front { left: 0; width: 600px; border-right: 2px solid var(--rule); }
  .card__back { left: 600px; width: 600px; }

  .wall {
    position: absolute; left: 30px; top: 40px; width: 543px; height: 345px;
    background: linear-gradient(135deg, var(--wall-b) 0%, var(--wall-a) 45%, var(--wall-c) 100%);
    border-radius: 6px;
  }
  .sign {
    position: absolute; left: 43px; top: 160px; width: 521px; height: 90px;
    background: var(--paper);
    border: 4px solid var(--sign-frame);
    outline: 3px solid var(--sign-edge);
    border-radius: 12px;
    display: flex; align-items: center; justify-content: center;
  }
  .sign__text {
    font-family: "Montserrat", sans-serif; font-weight: 600;
    font-size: 25px; letter-spacing: 1.5px; color: var(--ink);
  }

  .brand { position: absolute; top: 68px; left: 0; width: 600px; text-align: center; }
  .brand__name {
    font-family: "Josefin Sans", sans-serif; font-weight: 700;
    font-size: 38px; letter-spacing: 2px; color: var(--ink);
  }
  .brand__dashes { display: block; margin: 2px auto 0; }
  .brand__web {
    font-family: "Arimo", sans-serif; font-size: 20px; color: var(--ink); margin-top: 6px;
  }
  .contact {
    position: absolute; top: 184px; left: 0; width: 600px; text-align: center;
    font-family: "Arimo", sans-serif; font-size: 17px; line-height: 20.5px; color: var(--ink);
    font-style: normal;
  }
  .contact__lines { margin-top: 29px; }
  .mark {
    position: absolute; left: 48px; top: 296px; width: 76px; height: 76px;
    border-radius: 50%; background: var(--accent-mark);
  }
  .badge { position: absolute; left: 454px; top: 283px; }
</style>
</head>
<body>
<main class="sheet">

  <section class="card card--top card--brick">
    <div class="card__front">
      <div class="wall" role="img" aria-label="Terracotta brick wall illustration"></div>
      <div class="sign"><p class="sign__text">THANK YOU FOR YOUR PURCHASE</p></div>
    </div>
    <div class="card__back">
      <header class="brand">
        <h1 class="brand__name">LUMKIN PRINTS</h1>
        <svg class="brand__dashes" width="300" height="6" viewBox="0 0 300 6" aria-hidden="true">
          <line x1="0" y1="3" x2="300" y2="3" stroke="var(--dash-a)" stroke-width="4" stroke-dasharray="16 19"/>
          <line x1="35" y1="3" x2="300" y2="3" stroke="var(--dash-b)" stroke-width="4" stroke-dasharray="16 54"/>
        </svg>
        <p class="brand__web">www.lumkinprints.co.uk</p>
      </header>
      <address class="contact">
        <p>Lumkin Prints Ltd<br>Unit 8 Harrow Lane<br>Bramwell<br>Cheshire<br>CW9 4PL</p>
        <p class="contact__lines">01632 960418<br>sales@lumkinprints.co.uk</p>
      </address>
      <div class="mark" aria-hidden="true"></div>
      <svg class="badge" width="94" height="94" viewBox="0 0 94 94" aria-hidden="true">
        <circle cx="47" cy="47" r="45" fill="var(--badge-red)"/>
      </svg>
    </div>
  </section>

  <section class="card card--bottom card--tile">
    <div class="card__front">
      <div class="wall" role="img" aria-label="Green and white tiled brick wall illustration"></div>
      <div class="sign"><p class="sign__text">THANK YOU FOR YOUR PURCHASE</p></div>
    </div>
    <div class="card__back">
      <header class="brand">
        <h1 class="brand__name">LUMKIN PRINTS</h1>
        <svg class="brand__dashes" width="300" height="6" viewBox="0 0 300 6" aria-hidden="true">
          <line x1="0" y1="3" x2="300" y2="3" stroke="var(--dash-a)" stroke-width="4" stroke-dasharray="16 19"/>
          <line x1="35" y1="3" x2="300" y2="3" stroke="var(--dash-b)" stroke-width="4" stroke-dasharray="16 54"/>
        </svg>
        <p class="brand__web">www.lumkinprints.co.uk</p>
      </header>
      <address class="contact">
        <p>Lumkin Prints Ltd<br>Unit 8 Harrow Lane<br>Bramwell<br>Cheshire<br>CW9 4PL</p>
        <p class="contact__lines">01632 960418<br>sales@lumkinprints.co.uk</p>
      </address>
      <div class="mark" aria-hidden="true"></div>
      <svg class="badge" width="94" height="94" viewBox="0 0 94 94" aria-hidden="true">
        <circle cx="47" cy="47" r="45" fill="var(--badge-red)"/>
      </svg>
    </div>
  </section>

</main>
</body>
</html>
```